VELINTA Promotions - Business Card Design Project

We are looking for a classy business cards for Promotion Company based in Toronto, Canada named Velinta Promotions.

Velinta Promotions has an idea and vision to set high standard, be EXCLUSIVE and attract a group of people that will follow us through events we promote (night clubs, brand promotions, music events, and sport events)

We want to present a high standards and classy image to the others...
Updates

Target Market(s)

male/female age 25-40 Target: business owners young entrepreneur - clubing industry - media industry - promotion industry - marketing media industry

Industry/Entity Type

Events

Requirements
Must have
• business cards should be classy, make people feel exclusive , make people react ..

```html
<!DOCTYPE html>
<html lang="en">
<head>
<meta charset="UTF-8">
<title>Velinta Promotions – Business Cards</title>
<link rel="stylesheet" href="https://fonts.googleapis.com/css2?family=Cinzel:wght@400&family=Noto+Serif:wght@700&display=swap">
<style>
  :root {
    --page: #ffffff;
    --card-front: #e6e7e8;
    --card-back: #00bdf0;
    --brand-cyan: #2bb8e8;
    --ornament-light: #3cc0ee;
    --ornament-dark: #1598c8;
    --ink: #0a1a24;
  }
  * { margin: 0; padding: 0; box-sizing: border-box; }
  html, body {
    width: 1200px;
    height: 1152px;
    overflow: hidden;
    background: var(--page);
  }
  .canvas {
    position: relative;
    width: 1200px;
    height: 1152px;
  }
  .card {
    position: absolute;
    overflow: hidden;
  }
  .card--front {
    left: 0; top: 0;
    width: 868px; height: 536px;
    background: var(--card-front);
  }
  .card--back {
    left: 334px; top: 614px;
    width: 866px; height: 538px;
    background: var(--card-back);
  }
  .ornament { position: absolute; }
  .ornament--front-top {
    left: 520px; top: 10px; width: 350px; height: 320px;
  }
  .ornament--front-bottom {
    left: 0; top: 280px; width: 280px; height: 256px;
  }
  .ornament--back {
    left: 286px; top: 16px; width: 580px; height: 460px;
  }
  .brand {
    position: absolute;
    left: 72px; top: 196px;
    color: var(--brand-cyan);
    font-family: "Cinzel", "Times New Roman", serif;
    font-weight: 400;
  }
  .brand__row { display: flex; align-items: center; gap: 16px; }
  .brand__dot {
    width: 40px; height: 40px;
    border-radius: 50%;
    background: var(--brand-cyan);
  }
  .brand__name {
    font-size: 80px;
    line-height: 1;
    letter-spacing: 1px;
  }
  .brand__tagline {
    margin-left: 240px;
    margin-top: 2px;
    font-size: 19px;
    letter-spacing: 6px;
  }
  .contact {
    position: absolute;
    color: var(--ink);
    font-family: "Noto Serif", Georgia, serif;
    font-weight: 700;
  }
  .contact--main { left: 62px; top: 394px; }
  .contact__company { font-size: 32px; line-height: 1.2; }
  .contact__line { font-size: 20px; line-height: 1.6; }
  .contact--address {
    left: 486px; top: 396px;
    font-size: 19px;
    line-height: 1.38;
    letter-spacing: 0.5px;
  }
</style>
</head>
<body>
<div class="canvas">

  <section class="card card--front" aria-label="Business card front">
    <svg class="ornament ornament--front-top" role="img" aria-label="Flourish ornament in cyan" viewBox="0 0 350 320">
      <defs>
        <radialGradient id="flourishFront" cx="60%" cy="35%" r="65%">
          <stop offset="0" stop-color="var(--ornament-light)" stop-opacity="0.75"/>
          <stop offset="1" stop-color="var(--ornament-light)" stop-opacity="0"/>
        </radialGradient>
      </defs>
      <rect width="350" height="320" fill="url(#flourishFront)"/>
    </svg>
    <svg class="ornament ornament--front-bottom" role="img" aria-label="Flourish ornament in cyan" viewBox="0 0 280 256">
      <defs>
        <radialGradient id="flourishFrontLow" cx="30%" cy="70%" r="70%">
          <stop offset="0" stop-color="var(--ornament-light)" stop-opacity="0.75"/>
          <stop offset="1" stop-color="var(--ornament-light)" stop-opacity="0"/>
        </radialGradient>
      </defs>
      <rect width="280" height="256" fill="url(#flourishFrontLow)"/>
    </svg>

    <div class="brand">
      <div class="brand__row">
        <span class="brand__dot"></span>
        <span class="brand__name">VELINTA</span>
      </div>
      <div class="brand__tagline">PROMOTIONS</div>
    </div>
  </section>

  <section class="card card--back" aria-label="Business card back">
    <svg class="ornament ornament--back" role="img" aria-label="Tonal flourish ornament in deep blue" viewBox="0 0 580 460">
      <defs>
        <radialGradient id="flourishBack" cx="62%" cy="40%" r="60%">
          <stop offset="0" stop-color="var(--ornament-dark)" stop-opacity="0.8"/>
          <stop offset="1" stop-color="var(--ornament-dark)" stop-opacity="0"/>
        </radialGradient>
      </defs>
      <rect width="580" height="460" fill="url(#flourishBack)"/>
    </svg>

    <div class="contact contact--main">
      <p class="contact__company">Velinta Promotions</p>
      <p class="contact__line">Contact number: 123456</p>
      <p class="contact__line">www.velintapromotions.com</p>
    </div>

    <div class="contact contact--address">
      <p>address:xxxxxxxxxxxxxxxxxx</p>
      <p>xxxxxxxxxxxxxxxxxxxxxxxxx</p>
      <p>xxxxxxxxxxxxxxxxxxxxxxxxx</p>
    </div>
  </section>

</div>
</body>
</html>
```